The Brandling Firm

We need a new design for our letterhead and envelopes. We are a personal injury and criminal defense firm so we need something modern and clean, but more on the professional/traditional side. Our new logo has two colors and is attached to the file so we need something that works well with those colors/matches the design. The following information needs to be on the letterhead:
Phone: (555) 314-2716
Fax: (555) 314-5093
Toll-Free: (800) 555-0143
Post Office Box 4372
Alderbrook, NC 29548-4372
QVHarmCounselGroup.example
MarrowvaleTrialCounsel.example

Target Market(s)

Clients, government agencies, other law firms

Industry/Entity Type

Legal

Font styles to use
Sans Serif
Other font styles liked:
• Arial

Colors

Designer to choose colors to be used in the design.

Requirements
Must have
• Must look professional and clean, modern
Nice to have
• I would like to see a design that works with the logo but does not distract from the content that will be printed on it
Should not have
• Too many colors or crazy designs.

```html
<!DOCTYPE html>
<html lang="en">
<head>
<meta charset="utf-8">
<title>The Brandling Firm — Stationery</title>
<link rel="stylesheet" href="https://fonts.googleapis.com/css2?family=Open+Sans:wght@400;600&display=swap">
<style>
  :root {
    --backdrop: #595959;
    --paper: #ffffff;
    --ink: #3a3a3a;
    --brand-blue: #2e3192;
    --divider: #555555;
  }
  * { box-sizing: border-box; margin: 0; padding: 0; }
  html, body { width: 1200px; height: 904px; overflow: hidden; }
  body {
    position: relative;
    background: var(--backdrop);
    font-family: "Open Sans", Arial, sans-serif;
    color: var(--ink);
  }
  .sheet { position: absolute; background: var(--paper); }
  .letterhead { left: 50px; top: 114px; width: 528px; height: 746px; }
  .envelope-front { left: 610px; top: 263px; width: 544px; height: 271px; }
  .envelope-back { left: 610px; top: 576px; width: 544px; height: 271px; }

  .wordmark {
    position: absolute;
    display: flex;
    align-items: center;
    gap: 6px;
    font-size: 15px;
    line-height: 20px;
    font-weight: 600;
    color: var(--brand-blue);
    white-space: nowrap;
    letter-spacing: 0.02em;
  }
  .wordmark-dot { width: 9px; height: 9px; border-radius: 50%; background: var(--brand-blue); }
  .letterhead .wordmark { left: 50%; top: 57px; transform: translateX(-50%); }

  .letter-footer {
    position: absolute;
    left: 0; right: 0; top: 695px;
    display: flex;
    justify-content: center;
    align-items: flex-start;
    font-size: 8.5px;
    line-height: 11px;
    text-align: center;
  }
  .footer-col { padding: 0 14px; }
  .footer-col.address { width: 184px; }
  .footer-col.phones { width: 155px; }
  .footer-col.web { width: 188px; }
  .footer-rule { width: 1px; height: 30px; background: var(--divider); }

  .envelope-front .wordmark { left: 31px; top: 45px; }
  .return-address {
    position: absolute;
    left: 42px; top: 88px;
    width: 120px;
    font-size: 8.5px;
    line-height: 11px;
    text-align: center;
    white-space: nowrap;
    display: flex; flex-direction: column; align-items: center;
  }

  .flap { position: absolute; left: 0; top: 0; }
  .envelope-back .wordmark { left: 50%; top: 30px; transform: translateX(-50%); }
</style>
</head>
<body>

  <section class="sheet letterhead" aria-label="Letterhead">
    <div class="wordmark"><span class="wordmark-dot"></span>The Brandling Firm</div>
    <footer class="letter-footer">
      <div class="footer-col address">Post Office Box 4372<br>Alderbrook, NC 29548-4372</div>
      <div class="footer-rule"></div>
      <div class="footer-col phones">P: (555) 314-2716<br>F: (555) 314-5093<br>TF: (800) 555-0143</div>
      <div class="footer-rule"></div>
      <div class="footer-col web">QVHarmCounselGroup.example<br>MarrowvaleTrialCounsel.example</div>
    </footer>
  </section>

  <section class="sheet envelope-front" aria-label="Envelope front">
    <div class="wordmark"><span class="wordmark-dot"></span>The Brandling Firm</div>
    <div class="return-address">
      <span>Post Office Box 4372</span>
      <span>Alderbrook, NC 29548-4372</span>
    </div>
  </section>

  <section class="sheet envelope-back" aria-label="Envelope back">
    <svg class="flap" width="544" height="100" viewBox="0 0 544 100" aria-hidden="true">
      <defs>
        <linearGradient id="flapShade" x1="0" y1="0" x2="0" y2="1">
          <stop offset="0" stop-color="#000" stop-opacity="0.16"/>
          <stop offset="1" stop-color="#000" stop-opacity="0"/>
        </linearGradient>
      </defs>
      <path d="M0 6 Q10 46 50 56 L272 92 L494 56 Q534 46 544 6 L544 20 Q534 60 494 70 L272 104 L50 70 Q10 60 0 20 Z" fill="url(#flapShade)"/>
      <path d="M0 0 Q8 42 46 50 L272 80 L498 50 Q536 42 544 0 Z" fill="var(--paper)" stroke="#e2e2e2" stroke-width="1"/>
    </svg>
    <div class="wordmark"><span class="wordmark-dot"></span>The Brandling Firm</div>
  </section>

</body>
</html>
```